Need a 'country' kitchen feel for new bakery website

We need a website for a new bakery using the attached logo and similar color schemes throughout the site. The website can be based on LINUX or Windows servers.

I would like the website to look like recipe cards (i.e. index cards) without the lines and with 'tabs' at the top of each 'card' representing a different page (e.g. Main, Cookies, Cakes, Cupcakes, Misc., About, Contact Us) with a smooth transition between each of them. I'd also like to ensure the logo stays in the header as well as the phone number in the upper right hand corner (as well as contact us in the footer as well).

On each page I would like to be able to put some text at the top about our specialties and then be able to put in pictures under the blurb (if they could auto-rotate that would be great). But for each of the 'product' pages, I'd like the format to be consistent.

For the main page, I'd like to be able to put a blurb of text in and then have a rotating gallery (multiple pictures) underneath the blurb.

I would like to be able to add additional 'tabs'/pages in the future as we grow.

Lastly, I'd like to be able to add a Plumtalk logo so that visitors can click the logo and be sent to our Plumtalk site.

Any other questions, please let us know.

Bakery

Coded - Design and coding required

5+ page

• The navigation of the website needs to look and feel like index cards in a recipe box with 'tabs' at the top representing the different pages.
• Need to be able to add additional pages/tabs in the future.
• Smooth transition between pages.
• Need ability to put pictures and text in each card.
• An easy way for the visitors to be able to contact us (so contact info and Plumtalk link in there).
• Difficult navigation
• A lot of dark colors

```html
<!DOCTYPE html>
<html lang="en">
<head>
<meta charset="utf-8">
<title>Velvet Crescent Bakery</title>
<link href="https://fonts.googleapis.com/css2?family=Raleway:wght@400;500;600&display=swap" rel="stylesheet">
<style>
:root{
  --bg:#f7b0da;
  --accent:#d7266f;
  --accent-dark:#b8185a;
  --border:#dd3a86;
  --paper:#f8f6ef;
  --heading:#5c1233;
  --body:#3a3a3a;
  --white:#ffffff;
  --muted:#fbe3f1;
}
*{margin:0;padding:0;box-sizing:border-box}
html,body{width:968px;height:1200px;overflow:hidden}
body{background:var(--bg);font-family:'Raleway',sans-serif;color:var(--body);position:relative}
.abs{position:absolute}
.nav a{position:absolute;top:48px;height:29px;line-height:29px;font-size:13.5px;color:var(--white);text-decoration:none;font-weight:500}
.nav .active{background:var(--accent);padding:0 9px;border-radius:2px}
.phone{position:absolute;left:786px;top:48px;line-height:29px;font-size:13.5px;color:var(--white);font-weight:500;display:flex;align-items:center;gap:8px}
.logo-text{position:absolute;left:398px;top:32px;width:174px;height:116px;display:flex;align-items:center;justify-content:center;text-align:center;font-size:19px;line-height:22px;font-weight:600;color:var(--accent-dark)}
.heading{position:absolute;display:flex;align-items:center;gap:8px;font-size:20px;color:var(--heading);font-weight:500}
.heading .dot{width:13px;height:13px;border-radius:50%;background:var(--accent)}
.copy{position:absolute;font-size:12px;line-height:18.7px;color:var(--body)}
.item-title{position:absolute;font-size:15px;color:var(--accent);font-weight:500}
.thumb{position:absolute;width:93px;height:78px;border:2px solid #ddd}
.btn{position:absolute;height:34px;line-height:34px;background:var(--accent);color:var(--white);font-size:12px;font-weight:500;text-align:center;border-radius:2px;box-shadow:0 2px 0 var(--accent-dark)}
.hours{position:absolute;left:409px;top:984px;font-size:12.5px;color:var(--accent);line-height:20px}
.foot{position:absolute;color:var(--white);font-size:11px}
.foot-h{position:absolute;color:var(--white);font-size:15px;font-weight:500}
</style>
</head>
<body>

<nav class="nav">
  <a class="active" href="#" style="left:61px">Home</a>
  <a href="#" style="left:131px">Cookies</a>
  <a href="#" style="left:204px">Cakes</a>
  <a href="#" style="left:266px">Cupcakes</a>
  <a href="#" style="left:350px">Misc..</a>
  <a href="#" style="left:625px">About</a>
  <a href="#" style="left:686px">Contact Us</a>
</nav>
<div class="phone">
  <svg width="11" height="11" viewBox="0 0 24 24"><path fill="#fff" d="M6.6 10.8a15.1 15.1 0 0 0 6.6 6.6l2.2-2.2c.3-.3.7-.4 1-.2 1.1.4 2.3.6 3.6.6.6 0 1 .4 1 1V20c0 .6-.4 1-1 1A17 17 0 0 1 3 4c0-.6.4-1 1-1h3.5c.6 0 1 .4 1 1 0 1.3.2 2.5.6 3.6.1.3 0 .7-.2 1z"/></svg>
  1-800-555-0182
</div>

<svg class="abs" style="left:0;top:0" width="968" height="470">
  <defs>
    <linearGradient id="slideTone" x1="0" y1="0" x2="1" y2="1">
      <stop offset="0" stop-color="#f3a6c4"/>
      <stop offset=".5" stop-color="#f6d3d8"/>
      <stop offset="1" stop-color="#7cc4c9"/>
    </linearGradient>
  </defs>
  <polygon points="61,118 485,80 908,120 908,458 485,412 61,458" fill="#fff"/>
  <polygon role="img" aria-label="Photo of cupcakes topped with pink frosting and sugar roses" points="65,122 485,84 904,124 904,453 485,408 65,453" fill="url(#slideTone)"/>
  <polyline points="100,252 82,268 100,284" fill="none" stroke="#6b4450" stroke-width="6"/>
  <polyline points="867,252 885,268 867,284" fill="none" stroke="#6b4450" stroke-width="6"/>
  <ellipse cx="485" cy="90" rx="87" ry="58" fill="#fff" stroke="#e5e0e3" stroke-width="3"/>
</svg>
<div class="logo-text">Velvet Crescent<br>Bakery</div>

<svg class="abs" style="left:0;top:466px" width="968" height="600">
  <path d="M61,18 Q280,8 470,12 Q485,2 500,12 Q690,8 907,18 L907,588 Q690,578 500,580 Q485,590 470,580 Q280,578 61,588 Z" fill="var(--border)"/>
  <path d="M70,27 Q280,18 470,22 Q485,14 500,22 Q690,18 898,27 L898,580 Q690,570 500,572 Q485,580 470,572 Q280,570 70,580 Z" fill="var(--paper)"/>
  <line x1="484" y1="24" x2="484" y2="470" stroke="#ccc" stroke-dasharray="2 3"/>
  <line x1="89" y1="256" x2="468" y2="256" stroke="#ccc" stroke-dasharray="2 3"/>
  <line x1="89" y1="486" x2="880" y2="486" stroke="#ccc" stroke-dasharray="2 3"/>
</svg>

<div class="heading" style="left:89px;top:518px"><span class="dot"></span>Welcome to Our Website</div>
<p class="copy" style="left:89px;top:553px;width:368px">Praesent non dolor quis turpis placerat suscipit. Nunc quis velit magna. Lorem ipsum dolor sit amet, consectetur adipiscing elit. Vivamus et erat dolor. Vestibulum sollicitudin mollis ligula, dictum fringilla velit scelerisque a. Mauris ligula justo, mattis a pellentesque a, aliquam egestas magna. Donec fringilla velit sit amet quam tempus venenatis. Class aptent taciti sociosqu ad litora torquent per conubia nostra, per inceptos himenaeos. Mauris in est vitae neque ultrices tristique.</p>

<div class="heading" style="left:89px;top:736px"><span class="dot"></span>About Us</div>
<p class="copy" style="left:89px;top:771px;width:368px">Praesent non dolor quis turpis placerat suscipit. Nunc quis velit magna. Lorem ipsum dolor sit amet, consectetur adipiscing elit. Vivamus et erat dolor. Vestibulum sollicitudin mollis ligula, dictum fringilla velit scelerisque a. Mauris ligula justo, mattis a pellentesque a, aliquam egestas magna.</p>
<div class="btn" style="left:89px;top:888px;width:107px">Read More</div>

<div class="heading" style="left:507px;top:518px"><span class="dot"></span>Our Specialties</div>

<div class="thumb" role="img" aria-label="Photo of a cupcake with sprinkles" style="left:507px;top:558px;background:linear-gradient(135deg,#efe3d6,#d9a05c)"></div>
<div class="item-title" style="left:614px;top:554px">Cupcakes</div>
<p class="copy" style="left:614px;top:582px;width:272px">Class aptent taciti sociosqu ad litora torquent per conubia nostra, per inceptos himenaeos. Mauris in est vitae neque ultrices tristique.</p>

<div class="thumb" role="img" aria-label="Photo of a strawberry cake" style="left:507px;top:666px;background:linear-gradient(180deg,#d9392f,#f2e4c8)"></div>
<div class="item-title" style="left:614px;top:662px">Cakes</div>
<p class="copy" style="left:614px;top:690px;width:272px">Class aptent taciti sociosqu ad litora torquent per conubia nostra, per inceptos himenaeos. Mauris in est vitae neque ultrices tristique.</p>

<div class="thumb" role="img" aria-label="Photo of chocolate chip cookies" style="left:507px;top:774px;background:linear-gradient(135deg,#8a5a3a,#4a2c1c)"></div>
<div class="item-title" style="left:614px;top:770px">Cookies</div>
<p class="copy" style="left:614px;top:798px;width:272px">Class aptent taciti sociosqu ad litora torquent per conubia nostra, per inceptos himenaeos. Mauris in est vitae neque ultrices tristique.</p>

<div class="btn" style="left:507px;top:888px;width:123px">View All Products</div>

<div class="heading" style="left:218px;top:981px"><span class="dot"></span>Opening Hours</div>
<div class="hours">Monday - Friday:&nbsp;&nbsp; 8:00 - 22:0&nbsp; | &nbsp;Weekends:&nbsp;&nbsp;&nbsp;&nbsp; 9:00 - 23:00</div>

<div class="foot" style="left:61px;top:1090px">Home&nbsp; / &nbsp;Cookies&nbsp; / &nbsp;Cakes&nbsp; / &nbsp;Cupcakes&nbsp; / &nbsp;Misc..&nbsp; / &nbsp;About&nbsp; / &nbsp;Contact Us</div>
<div class="foot" style="left:61px;top:1130px;font-size:10px;line-height:18px">Copyright © 2016, Velvet Crescent Bakery<br>All Right Reserved</div>

<div class="foot-h" style="left:495px;top:1090px">Contact Us</div>
<div class="foot" style="left:495px;top:1117px;line-height:18px">412 Larkspur Lane<br>Bristol, B12 7QP</div>
<div class="foot" style="left:495px;top:1153px;display:flex;align-items:center;gap:6px">
  <svg width="11" height="9" viewBox="0 0 22 16"><rect width="22" height="16" rx="2" fill="#fff"/><polyline points="1,1 11,9 21,1" fill="none" stroke="var(--bg)" stroke-width="2"/></svg>
  hello@velvetcrescent.com
</div>

<div class="foot-h" style="left:690px;top:1090px">Call Us</div>
<div class="foot" style="left:690px;top:1118px;color:var(--accent);font-size:12px;font-weight:500">1-800-555-0182</div>

<div class="foot-h" style="left:823px;top:1090px">Connect Us</div>
<div class="foot" style="left:825px;top:1120px;display:flex;align-items:center;gap:6px;font-size:12px">
  <span style="width:12px;height:12px;background:#3b5a9a;display:inline-block"></span>Plumtalk
</div>

</body>
</html>
```